KWT Contracting services . Building and maintenance services, optic fibre installation

Business cards and logo design.I need a logo that I can use on business cards ,workwear and on my vehicles. I would like the KWT to be the main or larger text and contracting services to be the smaller or less important text.I like monograms, modern designs and repeating patterns symbols. I am also a Gemini and my favourite number is 22 so if this can be any inspiration to help with the design. Am thinking of the using German flag colours as a his is my family’s heritage. And the other 2 main colours I wear is black and white.But any ideas are appreciated.I do not need a design that is trade specific but a design that could be used for any business.

Target Market(s)

General public

Contact Information for Business Card

KWT Contracting Services ( front of business card)

(Back of business card)
Milo Brackwood
0471539264
Maintenance services
Optic fibre and data installation

Logo Text

Logo can just be pattern or monogram or incorporate KWT . I like the gemini star sign and the number 22

Colors
ec1f27
000000
fbee3e
ffffff

Requirements
Must have
• Logo and KWT Contracting Services on the front of business card
Nice to have
• Possible use of German flag colours.
• Modern design.
• Design to be able to be used on black or white background as I want to put it on clothing

```html
<!DOCTYPE html>
<html lang="en">
<head>
<meta charset="utf-8">
<title>KWT Contracting Services – Business Cards</title>
<link rel="stylesheet" href="https://fonts.googleapis.com/css2?family=Montserrat:wght@500;600;800&display=swap">
<style>
  :root {
    --canvas: #e9e7e3;
    --black: #0b0b0b;
    --white: #ffffff;
    --red: #ec1f27;
    --yellow: #fbce1f;
    --ink: #1d1d1d;
  }
  * { box-sizing: border-box; margin: 0; padding: 0; }
  html, body {
    width: 1200px; height: 1000px; overflow: hidden;
    background: var(--canvas);
    font-family: "Montserrat", Arial, sans-serif;
  }
  .canvas { position: relative; width: 1200px; height: 1000px; }

  .card {
    position: absolute; left: 280px;
    width: 640px; height: 366px;
    border-radius: 28px; overflow: hidden;
    box-shadow: 0 10px 30px rgba(0,0,0,.18);
  }
  .card--front { top: 90px; background: var(--black); }
  .card--back { top: 540px; background: var(--white); }

  /* brand lockup */
  .brand { position: absolute; display: flex; align-items: center; gap: 14px; }
  .brand__dot { border-radius: 50%; background: var(--yellow); flex: none; }
  .brand__text { display: flex; flex-direction: column; font-weight: 800; line-height: 1.1; white-space: nowrap; }
  .brand__name { letter-spacing: 2px; }
  .brand__tag { letter-spacing: 3px; }

  .card--front .brand { left: 50%; top: 50%; transform: translate(-50%, -50%); }
  .card--front .brand__dot { width: 30px; height: 30px; }
  .card--front .brand__text { color: var(--white); }
  .card--front .brand__name { font-size: 72px; }
  .card--front .brand__tag { font-size: 20px; }

  .card--back .brand { left: 40px; top: 100px; }
  .card--back .brand__dot { width: 20px; height: 20px; }
  .card--back .brand__text { color: var(--ink); }
  .card--back .brand__name { font-size: 46px; }
  .card--back .brand__tag { font-size: 14px; }

  /* holder name */
  .holder {
    position: absolute; right: 36px; top: 34px;
    display: flex; align-items: center; gap: 10px;
    font-weight: 600; font-size: 20px; color: var(--ink); text-transform: uppercase;
  }
  .holder__bar { width: 3px; height: 26px; background: var(--yellow); }

  /* contact */
  .contact { position: absolute; left: 40px; top: 232px; color: var(--ink); }
  .contact__phone { display: flex; align-items: center; gap: 8px; font-size: 20px; font-weight: 500; margin-bottom: 8px; }
  .contact__services {
    border-left: 3px solid var(--red); padding-left: 14px;
    font-size: 16px; font-weight: 500; line-height: 1.3;
  }
</style>
</head>
<body>
<main class="canvas">
  <section class="card card--front" aria-label="Business card front">
    <div class="brand">
      <span class="brand__dot"></span>
      <div class="brand__text">
        <span class="brand__name">KWT</span>
        <span class="brand__tag">CONTRACTING SERVICES</span>
      </div>
    </div>
  </section>

  <section class="card card--back" aria-label="Business card back">
    <div class="holder"><span>Milo Brackwood</span><span class="holder__bar"></span></div>

    <div class="brand">
      <span class="brand__dot"></span>
      <div class="brand__text">
        <span class="brand__name">KWT</span>
        <span class="brand__tag">CONTRACTING SERVICES</span>
      </div>
    </div>

    <div class="contact">
      <div class="contact__phone">
        <svg width="14" height="20" viewBox="0 0 14 20" aria-hidden="true">
          <rect x="1" y="1" width="12" height="18" rx="2" fill="none" stroke="#1d1d1d" stroke-width="2"/>
          <rect x="5" y="15" width="4" height="1.6" fill="#1d1d1d"/>
        </svg>
        <span>047 153 9264</span>
      </div>
      <div class="contact__services">
        Maintenance services<br>
        Optic fibre and<br>
        data installation
      </div>
    </div>
  </section>
</main>
</body>
</html>
```